Company service wheel graphic

A graphic demonstrating all the services the company offers.
I have hand drawn and written up on the attached the content that is required. Also attached is our company logo so you have a sense of the colour scheme of the logo.
This will eventually go into a company brochure, be used on our website etc.

Target Market(s)

Local GOvernment and other professionals who work in the sport, recreation and leisure industries

Industry/Entity Type

Sports, recreation, leisure, aquatics

Font styles to use
Other font styles liked:
• Calibri

Colors
0054AA
0677BA
7BADD7
CADEEF
E8F1F8

Requirements
Must have
• An eye catching graphic that captures all the information in the hand drawn atachement.
Nice to have
• Each quadrant in the circle to have its own colour, that links to the company logo

```html
<!DOCTYPE html>
<html lang="en">
<head>
<meta charset="utf-8">
<title>Service Wheel</title>
<link href="https://fonts.googleapis.com/css2?family=Montserrat:wght@700;800&family=Varela+Round&display=swap" rel="stylesheet">
<style>
  :root {
    --stage: #c0c0c0;
    --navy: #29235f;
    --ink: #1d1c33;
    --white: #ffffff;
    --quad-planning: #c2ddf0;
    --quad-management: #d6e8f5;
    --quad-participation: #ebf3fa;
    --quad-impact: #9cc3e3;
    --core-planning: #2a6c9e;
    --core-management: #3a8ac8;
    --core-participation: #6fa8d7;
    --core-impact: #1a4261;
    --hub: #0677ba;
    --tick: #3a3870;
  }
  * { margin: 0; padding: 0; box-sizing: border-box; }
  html, body { width: 1200px; height: 1200px; overflow: hidden; background: var(--stage); }
  .wheel { position: relative; width: 1200px; height: 1200px; }
  .wheel-art { position: absolute; inset: 0; }
  .ring-text {
    font-family: "Montserrat", sans-serif;
    font-weight: 800;
    font-size: 29px;
    fill: var(--white);
    letter-spacing: 0.5px;
  }
  .core-label, .hub-label, .pill-label {
    font-family: "Varela Round", sans-serif;
    fill: var(--white);
    text-anchor: middle;
  }
  .core-label { font-size: 15.5px; }
  .hub-label { font-size: 15px; }
  .pill-label { font-size: 15.5px; }
  .service-list {
    position: absolute;
    list-style: none;
    font-family: "Varela Round", sans-serif;
    font-size: 16px;
    line-height: 19px;
    color: var(--ink);
  }
  .service-list li { position: relative; padding-left: 13px; margin-bottom: 6px; white-space: nowrap; }
  .service-list .tick { position: absolute; left: 0; top: 4px; width: 10px; height: 10px; }
  .list-feasibility { left: 391px; top: 261px; }
  .list-revenue { left: 633px; top: 261px; }
  .list-design { left: 256px; top: 484px; }
  .list-finance { left: 776px; top: 484px; }
  .list-insights { left: 256px; top: 620px; }
  .list-monitoring { left: 776px; top: 620px; }
  .list-programs { left: 355px; top: 780px; }
  .list-kpis { left: 637px; top: 815px; }
</style>
</head>
<body>
<div class="wheel">
  <svg class="wheel-art" width="1200" height="1200" viewBox="0 0 1200 1200" aria-label="Service wheel">
    <defs>
      <clipPath id="inner-disc"><circle cx="600" cy="600" r="412"/></clipPath>
      <clipPath id="core-box"><rect x="466" y="467" width="268" height="267" rx="32"/></clipPath>
      <path id="arc-government" d="M195.0 452.6 A431 431 0 0 1 503.0 180.0"/>
      <path id="arc-managers" d="M562.4 170.6 A431 431 0 0 1 1007.5 459.7"/>
      <path id="arc-designers" d="M152.4 545.0 A451 451 0 0 0 611.8 1050.9"/>
      <path id="arc-providers" d="M651.1 1048.1 A451 451 0 0 0 1046.0 533.3"/>
    </defs>

    <circle cx="600" cy="600" r="474" fill="var(--white)"/>
    <circle cx="600" cy="600" r="471" fill="var(--navy)"/>

    <g class="quadrants" clip-path="url(#inner-disc)">
      <rect x="180" y="180" width="420" height="420" fill="var(--quad-planning)"/>
      <rect x="600" y="180" width="420" height="420" fill="var(--quad-management)"/>
      <rect x="180" y="600" width="420" height="420" fill="var(--quad-participation)"/>
      <rect x="600" y="600" width="420" height="420" fill="var(--quad-impact)"/>
    </g>

    <g class="ring-labels">
      <text class="ring-text"><textPath href="#arc-government" textLength="428" lengthAdjust="spacing">LOCAL + STATE GOVERNMENT</textPath></text>
      <text class="ring-text"><textPath href="#arc-managers" textLength="570" lengthAdjust="spacing">SPORT + LEISURE FACILITY MANAGERS</textPath></text>
      <text class="ring-text"><textPath href="#arc-designers" textLength="772" lengthAdjust="spacing">INVESTORS, DEVELOPERS, ARCHITECTS + DESIGNER</textPath></text>
      <text class="ring-text"><textPath href="#arc-providers" textLength="720" lengthAdjust="spacing">SPORT, RECREATION + COMMUNITY PROVIDERS</textPath></text>
      <circle cx="531" cy="164.4" r="10" fill="var(--white)"/>
      <circle cx="173.1" cy="489.6" r="10" fill="var(--white)"/>
      <circle cx="1026.9" cy="489.6" r="10" fill="var(--white)"/>
      <circle cx="630.8" cy="1039.9" r="5" fill="var(--white)"/>
    </g>

    <g class="core">
      <rect x="464" y="465" width="272" height="271" rx="34" fill="var(--white)"/>
      <g clip-path="url(#core-box)">
        <rect x="466" y="467" width="134" height="133" fill="var(--core-planning)"/>
        <rect x="600" y="467" width="134" height="133" fill="var(--core-management)"/>
        <rect x="466" y="600" width="134" height="134" fill="var(--core-participation)"/>
        <rect x="600" y="600" width="134" height="134" fill="var(--core-impact)"/>
      </g>
      <text class="core-label" x="530" y="510">Planning</text>
      <text class="core-label" x="668" y="510">Management</text>
      <text class="core-label" x="538" y="694">Growing</text>
      <text class="core-label" x="538" y="713">Participation</text>
      <text class="core-label" x="672" y="684">Community</text>
      <text class="core-label" x="673" y="703">impact +</text>
      <text class="core-label" x="673" y="722">outcomes</text>

      <circle cx="600" cy="600" r="71" fill="var(--hub)" stroke="var(--white)" stroke-width="3"/>
      <text class="hub-label" x="600" y="574">Community</text>
      <text class="hub-label" x="600" y="592">+</text>
      <text class="hub-label" x="600" y="612">Stakeholder</text>
      <text class="hub-label" x="600" y="631">Engagement</text>
    </g>

    <g class="pills">
      <rect x="409" y="429" width="382" height="37" rx="18.5" fill="var(--navy)" stroke="var(--white)" stroke-width="2.5"/>
      <text class="pill-label" x="600" y="452.5">Community, Aquatic + Recreation Facilities</text>
      <rect x="465" y="733" width="270" height="37" rx="18.5" fill="var(--navy)" stroke="var(--white)" stroke-width="2.5"/>
      <text class="pill-label" x="600" y="756.5">Community, Activation</text>
    </g>
  </svg>

  <ul class="service-list list-feasibility">
    <li><svg class="tick" viewBox="0 0 10 10"><circle cx="4.5" cy="5.5" r="3.6" fill="none" stroke="var(--tick)" stroke-width="1.2"/><path d="M2.6 5.3 L4.4 7.2 L9.2 1.2" fill="none" stroke="var(--tick)" stroke-width="1.6"/></svg>FeacibilityStudies</li>
    <li><svg class="tick" viewBox="0 0 10 10"><circle cx="4.5" cy="5.5" r="3.6" fill="none" stroke="var(--tick)" stroke-width="1.2"/><path d="M2.6 5.3 L4.4 7.2 L9.2 1.2" fill="none" stroke="var(--tick)" stroke-width="1.6"/></svg>Community +<br>stakeholder research</li>
    <li><svg class="tick" viewBox="0 0 10 10"><circle cx="4.5" cy="5.5" r="3.6" fill="none" stroke="var(--tick)" stroke-width="1.2"/><path d="M2.6 5.3 L4.4 7.2 L9.2 1.2" fill="none" stroke="var(--tick)" stroke-width="1.6"/></svg>Sport<br>+ recreation Strategies</li>
  </ul>

  <ul class="service-list list-revenue">
    <li><svg class="tick" viewBox="0 0 10 10"><circle cx="4.5" cy="5.5" r="3.6" fill="none" stroke="var(--tick)" stroke-width="1.2"/><path d="M2.6 5.3 L4.4 7.2 L9.2 1.2" fill="none" stroke="var(--tick)" stroke-width="1.6"/></svg>Activating<br>underutilised assets</li>
    <li><svg class="tick" viewBox="0 0 10 10"><circle cx="4.5" cy="5.5" r="3.6" fill="none" stroke="var(--tick)" stroke-width="1.2"/><path d="M2.6 5.3 L4.4 7.2 L9.2 1.2" fill="none" stroke="var(--tick)" stroke-width="1.6"/></svg>Income + revenue<br>generation strategies</li>
    <li><svg class="tick" viewBox="0 0 10 10"><circle cx="4.5" cy="5.5" r="3.6" fill="none" stroke="var(--tick)" stroke-width="1.2"/><path d="M2.6 5.3 L4.4 7.2 L9.2 1.2" fill="none" stroke="var(--tick)" stroke-width="1.6"/></svg>Mystery shopper + business<br>health checks</li>
  </ul>

  <ul class="service-list list-design">
    <li><svg class="tick" viewBox="0 0 10 10"><circle cx="4.5" cy="5.5" r="3.6" fill="none" stroke="var(--tick)" stroke-width="1.2"/><path d="M2.6 5.3 L4.4 7.2 L9.2 1.2" fill="none" stroke="var(--tick)" stroke-width="1.6"/></svg>Design Strategies</li>
    <li><svg class="tick" viewBox="0 0 10 10"><circle cx="4.5" cy="5.5" r="3.6" fill="none" stroke="var(--tick)" stroke-width="1.2"/><path d="M2.6 5.3 L4.4 7.2 L9.2 1.2" fill="none" stroke="var(--tick)" stroke-width="1.6"/></svg>Indoor<br>+ Outdoor spaces</li>
  </ul>

  <ul class="service-list list-finance">
    <li><svg class="tick" viewBox="0 0 10 10"><circle cx="4.5" cy="5.5" r="3.6" fill="none" stroke="var(--tick)" stroke-width="1.2"/><path d="M2.6 5.3 L4.4 7.2 L9.2 1.2" fill="none" stroke="var(--tick)" stroke-width="1.6"/></svg>Financial +<br>funding strategies</li>
    <li><svg class="tick" viewBox="0 0 10 10"><circle cx="4.5" cy="5.5" r="3.6" fill="none" stroke="var(--tick)" stroke-width="1.2"/><path d="M2.6 5.3 L4.4 7.2 L9.2 1.2" fill="none" stroke="var(--tick)" stroke-width="1.6"/></svg>Management&nbsp; Support</li>
    <li><svg class="tick" viewBox="0 0 10 10"><circle cx="4.5" cy="5.5" r="3.6" fill="none" stroke="var(--tick)" stroke-width="1.2"/><path d="M2.6 5.3 L4.4 7.2 L9.2 1.2" fill="none" stroke="var(--tick)" stroke-width="1.6"/></svg>Business planning</li>
  </ul>

  <ul class="service-list list-insights">
    <li><svg class="tick" viewBox="0 0 10 10"><circle cx="4.5" cy="5.5" r="3.6" fill="none" stroke="var(--tick)" stroke-width="1.2"/><path d="M2.6 5.3 L4.4 7.2 L9.2 1.2" fill="none" stroke="var(--tick)" stroke-width="1.6"/></svg>Trends + insights</li>
    <li><svg class="tick" viewBox="0 0 10 10"><circle cx="4.5" cy="5.5" r="3.6" fill="none" stroke="var(--tick)" stroke-width="1.2"/><path d="M2.6 5.3 L4.4 7.2 L9.2 1.2" fill="none" stroke="var(--tick)" stroke-width="1.6"/></svg>Health Profiling</li>
    <li><svg class="tick" viewBox="0 0 10 10"><circle cx="4.5" cy="5.5" r="3.6" fill="none" stroke="var(--tick)" stroke-width="1.2"/><path d="M2.6 5.3 L4.4 7.2 L9.2 1.2" fill="none" stroke="var(--tick)" stroke-width="1.6"/></svg>Active<br>recreation Strategies</li>
  </ul>

  <ul class="service-list list-monitoring">
    <li><svg class="tick" viewBox="0 0 10 10"><circle cx="4.5" cy="5.5" r="3.6" fill="none" stroke="var(--tick)" stroke-width="1.2"/><path d="M2.6 5.3 L4.4 7.2 L9.2 1.2" fill="none" stroke="var(--tick)" stroke-width="1.6"/></svg>Community<br>Impact Monitoring</li>
    <li><svg class="tick" viewBox="0 0 10 10"><circle cx="4.5" cy="5.5" r="3.6" fill="none" stroke="var(--tick)" stroke-width="1.2"/><path d="M2.6 5.3 L4.4 7.2 L9.2 1.2" fill="none" stroke="var(--tick)" stroke-width="1.6"/></svg>Social Value</li>
  </ul>

  <ul class="service-list list-programs">
    <li><svg class="tick" viewBox="0 0 10 10"><circle cx="4.5" cy="5.5" r="3.6" fill="none" stroke="var(--tick)" stroke-width="1.2"/><path d="M2.6 5.3 L4.4 7.2 L9.2 1.2" fill="none" stroke="var(--tick)" stroke-width="1.6"/></svg>Community<br>program development</li>
    <li><svg class="tick" viewBox="0 0 10 10"><circle cx="4.5" cy="5.5" r="3.6" fill="none" stroke="var(--tick)" stroke-width="1.2"/><path d="M2.6 5.3 L4.4 7.2 L9.2 1.2" fill="none" stroke="var(--tick)" stroke-width="1.6"/></svg>Physical activity strategies</li>
    <li><svg class="tick" viewBox="0 0 10 10"><circle cx="4.5" cy="5.5" r="3.6" fill="none" stroke="var(--tick)" stroke-width="1.2"/><path d="M2.6 5.3 L4.4 7.2 L9.2 1.2" fill="none" stroke="var(--tick)" stroke-width="1.6"/></svg>Specific&nbsp; Cohort Strategies</li>
    <li><svg class="tick" viewBox="0 0 10 10"><circle cx="4.5" cy="5.5" r="3.6" fill="none" stroke="var(--tick)" stroke-width="1.2"/><path d="M2.6 5.3 L4.4 7.2 L9.2 1.2" fill="none" stroke="var(--tick)" stroke-width="1.6"/></svg>Sport + Program<br>specific stratigies</li>
  </ul>

  <ul class="service-list list-kpis">
    <li><svg class="tick" viewBox="0 0 10 10"><circle cx="4.5" cy="5.5" r="3.6" fill="none" stroke="var(--tick)" stroke-width="1.2"/><path d="M2.6 5.3 L4.4 7.2 L9.2 1.2" fill="none" stroke="var(--tick)" stroke-width="1.6"/></svg>Community<br>outcomes + KPIs</li>
    <li><svg class="tick" viewBox="0 0 10 10"><circle cx="4.5" cy="5.5" r="3.6" fill="none" stroke="var(--tick)" stroke-width="1.2"/><path d="M2.6 5.3 L4.4 7.2 L9.2 1.2" fill="none" stroke="var(--tick)" stroke-width="1.6"/></svg>Contract Monitoring</li>
  </ul>
</div>
</body>
</html>
```